Popup Nightclub Grand Opening Flyer

We need to design a flyer for the grand opening of an upscale, exclusive nightclub called "Lanternfall". The design needs to be chic and exclusive. The background should be black and the text should primarily be white. We like minimalist designs.

Here is the text for the flyer
-
Velvetrope Atlanta Presents

Lanternfall (LOGO)

A Popup Nightclub Experience
For one night Only

Friday, October 18, 2013
Party begins at 9PM

INVITE ONLY

See invitation for location details
(Velvetrope Atlanta logo)

-
Examples we like

http://cdn2-b.brivelpost.com/sites/default/files/styles/image_content_width/hash/3d/fa/1472093815_4471_flyer.jpg?itok=R8kqWm2z

http://api.plovra.com/files/7Kqq-Tr82XXB3pQzJvmtR5HL2W719E4nbRtC6KLd4HsfM8Y2qTDK-VmjwDoNqLX4QBzTHD9nakRbVx3m-Pfq8htc3MDTWr5p4/2zelSaturdays.jpg

http://quenmar.com/wp-content/uploads/yootheme/widgetkit/gallery/2zel/2zel-gen_vroom4-01.jpg

Hi All, one thing that we are seeing that we don't like is on over emphasis on the phrase "a popup nightclub experience" please don't make this the largest thing on the flyer

Target Market(s)

Target market is 25-35 year olds who are affluent (rich) and like luxury brands

Requirements
Must have
• Dark Background
Nice to have
• Velvetrope Logo on the bottom
Modern text that isn't curvy
Should not have
• Curved text

```html
<!DOCTYPE html>
<html lang="en">
<head>
<meta charset="utf-8">
<title>Lanternfall – Popup Nightclub Flyer</title>
<link rel="stylesheet" href="https://fonts.googleapis.com/css2?family=Josefin+Sans:wght@300;400&family=Oswald:wght@300;500&family=Questrial&display=swap">
<style>
  :root {
    --ink: #000000;
    --panel-mid: #1c1c1c;
    --panel-edge: #070707;
    --white: #ffffff;
    --soft-white: #e9e9e9;
    --cyan: #1fc6ea;
    --silver: #c9c9c9;
  }
  * { margin: 0; padding: 0; box-sizing: border-box; }
  html, body { width: 1000px; height: 1200px; overflow: hidden; background: var(--ink); }
  .flyer {
    position: relative;
    width: 1000px;
    height: 1200px;
    overflow: hidden;
    background: radial-gradient(ellipse 55% 60% at 50% 42%, #161616 0%, #050505 70%, var(--ink) 100%);
    font-family: "Questrial", sans-serif;
    color: var(--white);
  }
  .backdrop-panel {
    position: absolute;
    left: 220px; top: 0;
    width: 560px; height: 1200px;
    background: radial-gradient(ellipse 80% 55% at 50% 40%, var(--panel-mid) 0%, #0d0d0d 60%, var(--panel-edge) 100%);
  }
  .line {
    position: absolute;
    left: 0; width: 1000px;
    text-align: center;
    white-space: nowrap;
  }
  .presenter-name {
    top: 108px;
    font-size: 44px;
    letter-spacing: 7px;
    color: var(--cyan);
  }
  .presenter-note {
    top: 160px;
    font-size: 18px;
    letter-spacing: 4px;
    color: var(--soft-white);
  }
  .dot-row {
    position: absolute;
    left: 50%;
    transform: translateX(-50%);
    width: 438px;
    height: 12px;
    background-image: radial-gradient(circle, var(--white) 4.6px, transparent 5.4px);
    background-size: 21.9px 12px;
  }
  .dot-row--top { top: 192px; }
  .dot-row--a { top: 771px; }
  .dot-row--b { top: 827px; }
  .dot-row--c { top: 976px; }

  .venue-badge {
    position: absolute;
    left: 263px; top: 253px;
    width: 474px; height: 474px;
  }
  .venue-name {
    top: 468px;
    font-family: "Josefin Sans", sans-serif;
    font-weight: 300;
    font-size: 52px;
    letter-spacing: 8px;
    color: var(--white);
  }
  .access {
    top: 790px;
    font-family: "Oswald", sans-serif;
    font-weight: 300;
    font-size: 27px;
    letter-spacing: 7px;
    color: var(--cyan);
    line-height: 1;
  }
  .concept {
    top: 848px;
    font-size: 25px;
    letter-spacing: 1px;
  }
  .one-night {
    top: 878px;
    font-size: 33px;
  }
  .one-night .bullet { color: var(--cyan); }
  .date {
    top: 912px;
    font-family: "Oswald", sans-serif;
    font-size: 50px;
    line-height: 1.2;
    color: var(--cyan);
  }
  .date .weekday { font-weight: 300; }
  .date .day { font-weight: 500; }
  .start-time {
    top: 993px;
    font-size: 25px;
    letter-spacing: 7px;
  }
  .location-note {
    top: 1069px;
    font-size: 14px;
    font-weight: 700;
    letter-spacing: 7px;
    font-family: "Josefin Sans", sans-serif;
  }
  .footer-brand {
    top: 1104px;
    font-size: 32px;
    letter-spacing: 6px;
    color: var(--white);
  }
</style>
</head>
<body>
<main class="flyer">
  <div class="backdrop-panel" role="img" aria-label="Dark wood-grain texture panel"></div>

  <p class="line presenter-name">VELVETROPE ATLANTA</p>
  <p class="line presenter-note">PRESENTS</p>
  <div class="dot-row dot-row--top"></div>

  <svg class="venue-badge" viewBox="0 0 474 474" aria-hidden="true">
    <defs>
      <radialGradient id="badge-fill" cx="50%" cy="35%" r="65%">
        <stop offset="0%" stop-color="#3a3a3a"/>
        <stop offset="100%" stop-color="#0a0a0a"/>
      </radialGradient>
    </defs>
    <circle cx="237" cy="237" r="232" fill="url(#badge-fill)" stroke="var(--silver)" stroke-width="8"/>
  </svg>
  <p class="line venue-name">LANTERNFALL</p>

  <div class="dot-row dot-row--a"></div>
  <p class="line access">INVITE ONLY</p>
  <div class="dot-row dot-row--b"></div>

  <p class="line concept">A POPUP NIGHTCLUB EXPERIENCE</p>
  <p class="line one-night"><span class="bullet">•</span>FOR ONE NIGHT ONLY<span class="bullet">•</span></p>
  <p class="line date"><span class="weekday">FRIDAY</span> <span class="day">OCTOBER 18,2013</span></p>
  <div class="dot-row dot-row--c"></div>
  <p class="line start-time">PARTY BEGINS @ 9PM</p>

  <p class="line location-note">SEE INVITATION FOR LOCATION DETAILS</p>
  <p class="line footer-brand">VELVETROPE ATLANTA</p>
</main>
</body>
</html>
```